Business card design needed

We need a business card for a new business. We are called Little Crew Wearhouse, and we make replica kid size clothing, mainly hi vis shirts, work trousers and shorts. Our long term goal is to include clothing for numerous trades and professions, for our littlest Aussies. We would like a kid friendly card using navy blue, bright orange, bright yellow and bright pink. We haven't set up our web page yet because we want to base it on our final business card design.
Updates

Industry/Entity Type

Clothing

```html
<!DOCTYPE html>
<html lang="en">
<head>
<meta charset="utf-8">
<title>Little Crew Wearhouse – Business Card</title>
<link rel="stylesheet" href="https://fonts.googleapis.com/css2?family=Indie+Flower&display=swap">
<style>
  :root {
    --paper: #ffffff;
    --ink: #141414;
    --stripe-blue: #2a84ff;
    --stripe-orange: #ff3a10;
    --stripe-yellow: #ffff00;
    --stripe-pink: #ff00ff;
    --brand-blue: #2a84ff;
    --trail-tint: #ededed;
  }
  * { margin: 0; padding: 0; box-sizing: border-box; }
  html, body {
    width: 1200px;
    height: 736px;
    overflow: hidden;
    background: var(--paper);
  }
  .card {
    position: relative;
    width: 1200px;
    height: 736px;
    background: var(--paper);
    overflow: hidden;
    font-family: "Indie Flower", cursive;
  }
  .stripes {
    position: absolute;
    top: 0;
    left: 4px;
    height: 736px;
    display: flex;
  }
  .stripe { width: 44px; height: 100%; }
  .stripe--blue { background: var(--stripe-blue); }
  .stripe--orange { background: var(--stripe-orange); }
  .stripe--yellow { background: var(--stripe-yellow); }
  .stripe--pink { background: var(--stripe-pink); }

  .brand-name {
    position: absolute;
    left: 535px;
    top: 150px;
    font-size: 64px;
    font-weight: 400;
    line-height: 1;
    color: var(--brand-blue);
    white-space: nowrap;
  }
  .contact {
    position: absolute;
    left: 535px;
    top: 262px;
    list-style: none;
    color: var(--ink);
    font-size: 42px;
    line-height: 62px;
    white-space: nowrap;
  }
  .trail-area {
    position: absolute;
    left: 182px;
    top: 528px;
    width: 1018px;
    height: 208px;
    background: linear-gradient(180deg, var(--paper) 0%, var(--trail-tint) 100%);
  }
</style>
</head>
<body>
  <div class="card">
    <div class="stripes" aria-hidden="true">
      <div class="stripe stripe--blue"></div>
      <div class="stripe stripe--orange"></div>
      <div class="stripe stripe--yellow"></div>
      <div class="stripe stripe--pink"></div>
    </div>

    <h1 class="brand-name">Little Crew Wearhouse</h1>

    <ul class="contact">
      <li class="contact__phone">Phone: 555018274</li>
      <li class="contact__email">email: crew@littlecrew.example</li>
      <li class="contact__fax">fax: 55501827-40</li>
    </ul>

    <div class="trail-area" role="img" aria-label="Decorative dashed looping trail running along the bottom of the card"></div>
  </div>
</body>
</html>
```